Coralvale Jukebox and Jumping Castle Hire

Hi folks,
This is for a new business based in Brisbane(Australia), the business hires, jukeboxes, inflatable games(mostly jumping castles) and slushy/cocktail machines.
I want the website to appeal to people looking to party. Does that sound too simplistic?
It should be simple to navigate, I require only the front page but make it easy to get to the rest of the site.
Modern, exciting and funky, think rock band or concert promoter.
We are trying to sell packages of products, there should be several packages visible on the front page without looking cluttered.
Link to jukebox song list.
Friendlane, pondlet etc.
I am currently on holidays so I have a fair amount of time to get this project done, it says 10 days I hope to have it done much sooner.

Reason: So far there is no design that I am happy with. I am after a website for Jukeboxes, it should have a rock concert feel.

Ages 20 to 50

Business

• Think rock band type website, black with bold color highlight.
• Plain or bland color.
Pictures of Brisbane or any other city.
Vexaro map or any other location type map.

```html
<!DOCTYPE html>
<html lang="en">
<head>
<meta charset="utf-8">
<title>Jukebox &amp; Jumping Castle Hire</title>
<link rel="stylesheet" href="https://fonts.googleapis.com/css2?family=Varela+Round&display=swap">
<style>
  :root {
    --bg-top: #050505;
    --bg-mid: #151515;
    --ink: #b9bcc0;
    --ink-strong: #ececec;
    --brand: #ffffff;
    --heading: #27b4f0;
    --nav-red: #d4141b;
    --nav-orange: #ef8a12;
    --nav-green: #2fa316;
    --nav-cyan: #1baee3;
    --nav-purple: #b043e0;
    --nav-yellow: #f1bb08;
    --pack-red: #ff3b3f;
    --btn-green: #24a019;
    --btn-grey: #5a5a5a;
    --panel: #1e1e1e;
    --panel-edge: #27b4f0;
    --row: #2b2b2b;
    --time: #ff4a4e;
    --footer: #000000;
    --footer-text: #a9a9a9;
    --news: #27b4f0;
    --signup: #f1bb08;
    --rule: #333333;
  }
  * { margin: 0; padding: 0; box-sizing: border-box; }
  html, body { width: 956px; height: 1200px; overflow: hidden; }
  body {
    position: relative;
    font-family: "Varela Round", "Trebuchet MS", sans-serif;
    color: var(--ink);
    background: linear-gradient(180deg, var(--bg-top) 0px, var(--bg-mid) 460px, #101010 100%);
  }
  .abs { position: absolute; }

  .brand-name { left: 58px; top: 16px; font-size: 20px; line-height: 24px; color: var(--brand); }

  .connect { right: 59px; top: 32px; display: flex; align-items: center; gap: 7px; font-size: 11px; color: var(--ink-strong); }
  .connect .label { margin-right: 4px; }
  .social { display: flex; align-items: center; gap: 3px; font-size: 10px; color: var(--ink); text-decoration: none; }
  .social i { width: 13px; height: 13px; border-radius: 50%; display: inline-block; }
  .social.friendlane i { background: #3c6cc0; }
  .social.pondlet i { background: #2aa7e3; }
  .social.vexaro i { background: #777; }
  .social.feed i { background: #f08a1c; }
  .social.tubely i { background: #e02a20; }

  .main-nav { left: 58px; top: 82px; width: 839px; display: flex; justify-content: space-between; }
  .main-nav a { width: 122px; height: 29px; line-height: 29px; text-align: center; color: #fff; font-size: 12px; text-decoration: none; }
  .nav-red { background: var(--nav-red); }
  .nav-orange { background: var(--nav-orange); }
  .nav-green { background: var(--nav-green); }
  .nav-cyan { background: var(--nav-cyan); }
  .nav-purple { background: var(--nav-purple); }
  .nav-yellow { background: var(--nav-yellow); }

  .hero { left: 58px; top: 121px; width: 839px; height: 300px; background: #222; border: 1px solid #333; padding: 3px; }
  .hero-photo { width: 100%; height: 100%; background: linear-gradient(90deg, #e9801c 0%, #f0b020 35%, #c98a2a 55%, #5b8f3c 70%, #e5543a 85%, #4c8a3a 100%); }
  .hero-dots { left: 444px; top: 384px; display: flex; gap: 5px; }
  .hero-dots span { width: 13px; height: 13px; border-radius: 50%; background: #111; }
  .hero-dots span.active { background: #fff; }

  .welcome-photo { left: 58px; top: 456px; width: 216px; height: 128px; background: linear-gradient(180deg, #9ab8d6 0%, #f3d9a8 35%, #8fa3b5 60%, #6f8d4d 85%, #4d6b33 100%); }
  .section-title { font-size: 18px; color: var(--heading); font-weight: 400; line-height: 22px; }
  .welcome-title { left: 294px; top: 452px; }
  .welcome-text { left: 294px; top: 484px; width: 604px; font-size: 9.4px; line-height: 17px; }
  .btn { display: inline-block; color: #fff; font-size: 9px; text-transform: uppercase; text-decoration: none; text-align: center; }
  .btn-read { left: 294px; top: 561px; width: 72px; height: 24px; line-height: 24px; background: var(--btn-grey); }

  .divider { left: 58px; top: 610px; width: 839px; height: 1px; background: var(--rule); }

  .packages-title { left: 58px; top: 629px; }
  .package { top: 665px; width: 194px; }
  .package-photo { width: 194px; height: 101px; }
  .package h3 { margin-top: 9px; font-size: 14px; line-height: 17px; font-weight: 400; color: var(--pack-red); }
  .package p { margin-top: 2px; font-size: 9.4px; line-height: 17px; }
  .btn-details { margin-top: 13px; width: 80px; height: 23px; line-height: 23px; background: var(--btn-green); }

  .panel { left: 58px; top: 885px; width: 839px; height: 202px; background: var(--panel); border-top: 3px solid var(--panel-edge); }
  .songs-title { left: 77px; top: 900px; }
  .song-list { list-style: none; width: 245px; }
  .song-list li { height: 28px; margin-bottom: 4px; background: var(--row); display: flex; align-items: center; font-size: 9.6px; color: var(--ink-strong); padding-left: 13px; }
  .song-list .num { width: 16px; }
  .song-list .name { width: 170px; }
  .song-list .time { color: var(--time); }
  .songs-left { left: 77px; top: 933px; }
  .songs-right { left: 334px; top: 933px; }
  .gallery-title { left: 620px; top: 900px; }
  .thumb { width: 76px; height: 60px; }

  .footer { left: 0; top: 1105px; width: 956px; height: 95px; background: var(--footer); border-top: 1px solid #262626; }
  .footer-nav { left: 58px; top: 1124px; font-size: 10px; color: var(--footer-text); }
  .footer-nav a { color: var(--footer-text); text-decoration: none; }
  .footer-nav .sep { margin: 0 9px; }
  .copyright { left: 58px; top: 1161px; font-size: 9px; color: #7a7a7a; }
  .news-title { left: 632px; top: 1123px; font-size: 12px; font-weight: 400; color: var(--news); }
  .news-input { left: 632px; top: 1148px; width: 194px; height: 26px; background: #fff; border: none; font-family: inherit; font-size: 9px; color: #888; padding-left: 10px; }
  .news-btn { left: 837px; top: 1148px; width: 61px; height: 26px; background: var(--signup); border: none; font-family: inherit; font-size: 11px; color: #fff; }
</style>
</head>
<body>

  <div class="abs brand-name">Jukebox &amp; Jumping<br>Castle Hire</div>

  <div class="abs connect">
    <span class="label">Connect Us:</span>
    <a class="social friendlane" href="#"><i></i>Friendlane</a>
    <a class="social pondlet" href="#"><i></i>pondlet</a>
    <a class="social vexaro" href="#"><i></i>Vexaro</a>
    <a class="social feed" href="#"><i></i>Feed</a>
    <a class="social tubely" href="#"><i></i>Tubely</a>
  </div>

  <nav class="abs main-nav">
    <a class="nav-red" href="#">Home</a>
    <a class="nav-orange" href="#">Juke Box</a>
    <a class="nav-green" href="#">Jumping Castle</a>
    <a class="nav-cyan" href="#">Our Packages</a>
    <a class="nav-purple" href="#">Song List</a>
    <a class="nav-yellow" href="#">Contact Us</a>
  </nav>

  <div class="abs hero">
    <div class="hero-photo" role="img" aria-label="Children playing on colourful inflatable jumping castles in a garden"></div>
  </div>
  <div class="abs hero-dots"><span class="active"></span><span></span><span></span><span></span></div>

  <div class="abs welcome-photo" role="img" aria-label="City skyline by a river at sunset with a park in front"></div>
  <h2 class="abs section-title welcome-title">Welcome to Our Website</h2>
  <p class="abs welcome-text">Aliquam molestie, mi et imperdiet euismod, dui purus auctor tellus, et interdum lacus lectus et ante. Sed accumsan sollicitudin sapien, sit amet adipiscing turpis gravida ac. In congue, neque ac lobortis volutpat, libero mauris varius mi, vitae suscipit ipsum ligula vitae risus. Duis aliquam nibh a dui iaculis viverra id a velit. Vivamus egestas risus in magna varius commodo. Sed semper viverra egestas. Etiam pretium porttitor lectus, vel ornare neque porta volutpat.</p>
  <a class="abs btn btn-read" href="#">Read More</a>

  <div class="abs divider"></div>

  <h2 class="abs section-title packages-title">Our Packages</h2>

  <article class="abs package" style="left:58px">
    <div class="package-photo" role="img" aria-label="Large multicoloured inflatable castle with towers" style="background:linear-gradient(180deg,#b9c3cc 0%,#d9453a 45%,#2d6fc0 80%,#5a7a9a 100%)"></div>
    <h3>Package 1</h3>
    <p>Vestibulum ante ipsum primis in faucibus orci luctus et ultrices posuere cubilia..</p>
    <a class="btn btn-details" href="#">View Details</a>
  </article>
  <article class="abs package" style="left:274px">
    <div class="package-photo" role="img" aria-label="Yellow and red inflatable castle with guests in a park" style="background:linear-gradient(180deg,#4e7a3a 0%,#e8b52a 40%,#d7542c 65%,#6b6b4a 100%)"></div>
    <h3>Package 2</h3>
    <p>Vestibulum ante ipsum primis in faucibus orci luctus et ultrices posuere cubilia..</p>
    <a class="btn btn-details" href="#">View Details</a>
  </article>
  <article class="abs package" style="left:489px">
    <div class="package-photo" role="img" aria-label="Colourful inflatable castle with slide on a lawn" style="background:linear-gradient(180deg,#6aa7e0 0%,#9fc7ec 35%,#e8c230 55%,#2f8fd0 75%,#5f9a3e 100%)"></div>
    <h3>Package 3</h3>
    <p>Vestibulum ante ipsum primis in faucibus orci luctus et ultrices posuere cubilia..</p>
    <a class="btn btn-details" href="#">View Details</a>
  </article>
  <article class="abs package" style="left:704px">
    <div class="package-photo" role="img" aria-label="Wide inflatable castle with towers outside a building" style="background:linear-gradient(180deg,#8a9a8a 0%,#3f8a3a 40%,#e0c030 60%,#3a70c0 85%,#2f5a2f 100%)"></div>
    <h3>Package 4</h3>
    <p>Vestibulum ante ipsum primis in faucibus orci luctus et ultrices posuere cubilia..</p>
    <a class="btn btn-details" href="#">View Details</a>
  </article>

  <section class="abs panel"></section>
  <h2 class="abs section-title songs-title">Jukebox Songs</h2>
  <ol class="abs song-list songs-left">
    <li><span class="num">1.</span><span class="name">Duis aliquam nibh a dui iaculis</span><span class="time">3:45</span></li>
    <li><span class="num">2.</span><span class="name">Duis aliquam nibh a dui iaculis</span><span class="time">3:45</span></li>
    <li><span class="num">3.</span><span class="name">Duis aliquam nibh a dui iaculis</span><span class="time">3:45</span></li>
    <li><span class="num">4.</span><span class="name">Duis aliquam nibh a dui iaculis</span><span class="time">3:45</span></li>
  </ol>
  <ol class="abs song-list songs-right">
    <li><span class="num">5.</span><span class="name">Duis aliquam nibh a dui iaculis</span><span class="time">3:45</span></li>
    <li><span class="num">6.</span><span class="name">Duis aliquam nibh a dui iaculis</span><span class="time">3:45</span></li>
    <li><span class="num">7.</span><span class="name">Duis aliquam nibh a dui iaculis</span><span class="time">3:45</span></li>
    <li><span class="num">8.</span><span class="name">Duis aliquam nibh a dui iaculis</span><span class="time">3:45</span></li>
  </ol>

  <h2 class="abs section-title gallery-title">Photo Gallery</h2>
  <div class="abs thumb" style="left:620px;top:932px;background:linear-gradient(135deg,#d92a2a,#f0c020 50%,#2a6fd0)" role="img" aria-label="Red and yellow bouncy castle"></div>
  <div class="abs thumb" style="left:708px;top:932px;background:linear-gradient(180deg,#c9c9c9,#c8323a 45%,#b0503a)" role="img" aria-label="Red inflatable castle at an outdoor event"></div>
  <div class="abs thumb" style="left:796px;top:932px;background:linear-gradient(135deg,#4aa8e0,#e8603a 50%,#2f8a3a)" role="img" aria-label="Children jumping inside an inflatable"></div>
  <div class="abs thumb" style="left:620px;top:999px;background:linear-gradient(180deg,#6a9a4a,#e8c030 45%,#3a8a3a)" role="img" aria-label="Small bouncy castle on grass"></div>
  <div class="abs thumb" style="left:708px;top:999px;background:linear-gradient(135deg,#3a8a3a,#d83a2a 45%,#2a6fc0)" role="img" aria-label="Inflatable slide in red, yellow and blue"></div>
  <div class="abs thumb" style="left:796px;top:999px;background:linear-gradient(180deg,#5a9ae0,#e8b030 50%,#4a8a3a)" role="img" aria-label="Colourful castle with turrets under blue sky"></div>

  <footer class="abs footer"></footer>
  <nav class="abs footer-nav">
    <a href="#">Home</a><span class="sep">/</span><a href="#">About Us</a><span class="sep">/</span><a href="#">Services</a><span class="sep">/</span><a href="#">Testimonials</a><span class="sep">/</span><a href="#">News</a><span class="sep">/</span><a href="#">Contact Us</a>
  </nav>
  <p class="abs copyright">Copyright © 2014. Company Name. All Right Reserved</p>
  <h3 class="abs news-title">Newsletter Signup</h3>
  <input class="abs news-input" type="text" placeholder="Enter Email Address" aria-label="Email address">
  <button class="abs news-btn" type="button">Sign Up</button>

</body>
</html>
```